Business Card Design

We are starting up a new Family run Business mainly offering a Free House Clearance service. We also offer the following chargeable services which include a Removals Service, Delivery and Collection of Items sold or purchased on Bidloft, Swapwren etc, including Motorcycles, Piano's, Furniture, Electrical appliances.
As there are a few Companies offering similar services we need to stand out and show what we do at a glance while appearing Professional and approachable
Updates

TidyNests

i  am liking some of the colours and designs so far but would like to see a few of our services listed as 1 or 2 have already done if this is possible and maybe some emphasis on the FREE House Clearance. thank you 
best regards
derek

Target Market(s)

Commercial and Domestic Tenants and Landlords aswell as Families looking for a friendly sympathetic clearance service after bereavement

Industry/Entity Type

Business

Contact Information for Business Card

TidyNests,
HouseClearance and Removals,
Marlow Dene
LM47 2QT
Tel: 07815239604
Email: enquiries@tidynests-example.info

```html
<!DOCTYPE html>
<html lang="en">
<head>
<meta charset="utf-8">
<title>TidyNests Business Card</title>
<link href="https://fonts.googleapis.com/css2?family=Lato:wght@400;700;900&display=swap" rel="stylesheet">
<style>
  :root {
    --backdrop: #3b3532;
    --card: #060606;
    --accent: #1f9ee3;
    --ink-light: #f2f2f2;
    --ink-soft: #cfcfcf;
  }
  * { box-sizing: border-box; margin: 0; padding: 0; }
  html, body {
    width: 1200px;
    height: 716px;
    overflow: hidden;
    background: var(--backdrop);
    font-family: "Lato", Arial, sans-serif;
  }
  .sheet {
    position: relative;
    width: 1200px;
    height: 716px;
    display: flex;
    align-items: center;
    justify-content: center;
    gap: 48px;
  }
  .card {
    position: relative;
    width: 520px;
    height: 300px;
    background: var(--card);
    box-shadow: 0 10px 28px rgba(0,0,0,0.45);
    overflow: hidden;
  }
  .card-front__headline {
    position: absolute;
    left: 62px;
    top: 96px;
    color: var(--accent);
    font-size: 30px;
    font-weight: 700;
    letter-spacing: -0.2px;
    white-space: nowrap;
  }
  .card-back__name {
    position: absolute;
    left: 40px;
    top: 108px;
    color: var(--ink-light);
    font-size: 24px;
    font-weight: 900;
    letter-spacing: 4px;
    text-transform: uppercase;
    white-space: nowrap;
  }
  .card-back__tagline {
    position: absolute;
    right: 38px;
    top: 150px;
    color: var(--ink-soft);
    font-size: 16px;
    font-weight: 400;
    letter-spacing: 0.6px;
    white-space: nowrap;
  }
  .card-back__rule {
    position: absolute;
    left: 0;
    right: 34px;
    top: 178px;
    height: 2px;
    background: var(--accent);
  }
  .card-back__contacts {
    position: absolute;
    left: 40px;
    right: 34px;
    top: 190px;
    display: flex;
    align-items: center;
    justify-content: space-between;
    color: var(--accent);
    font-size: 10.5px;
    letter-spacing: 0.2px;
    white-space: nowrap;
  }
  .card-back__divider {
    display: block;
    width: 1px;
    height: 10px;
    background: var(--ink-soft);
  }
</style>
</head>
<body>
  <main class="sheet">
    <section class="card card-front" aria-label="Business card front">
      <p class="card-front__headline">FREE House Clearance</p>
    </section>

    <section class="card card-back" aria-label="Business card back">
      <h1 class="card-back__name">TidyNests</h1>
      <p class="card-back__tagline">House Clearance and Removals</p>
      <div class="card-back__rule"></div>
      <div class="card-back__contacts">
        <span class="card-back__address">Marlow Dene LM47 2QT</span>
        <span class="card-back__divider"></span>
        <span class="card-back__phone">T: 07815239604</span>
        <span class="card-back__divider"></span>
        <span class="card-back__email">E: enquiries@tidynests-example.info</span>
      </div>
    </section>
  </main>
</body>
</html>
```